Kestrel Roofing & Restoration Business Card Design

Lookiing for a double sided business card design that will have rounded corners, will look good with Spot UV, Soft Laminate, or Gloss
Front of card should have Logo, Name and Contact Info, License numbers
Back of card should have Logo, maybe other small details

```html
<!DOCTYPE html>
<html lang="en">
<head>
<meta charset="utf-8">
<title>Kestrel Roofing &amp; Restoration – Business Card</title>
<link rel="stylesheet" href="https://fonts.googleapis.com/css2?family=Poppins:wght@400;500;600;700&display=swap">
<style>
  :root {
    --canvas: #16161a;
    --card: #232427;
    --card-pattern: #1f2023;
    --ink: #ffffff;
    --ink-soft: #d9dadd;
    --accent: #1aa0e0;
  }
  * { box-sizing: border-box; margin: 0; padding: 0; }
  html, body {
    width: 1200px; height: 800px; overflow: hidden;
    background: var(--canvas);
    font-family: "Poppins", sans-serif;
    color: var(--ink);
  }
  .stage {
    position: relative; width: 1200px; height: 800px;
    display: flex; align-items: center; justify-content: center; gap: 60px;
  }
  .card {
    position: relative; width: 520px; height: 300px;
    background: var(--card); border-radius: 24px; overflow: hidden;
    box-shadow: 0 18px 40px rgba(0,0,0,.55);
  }
  /* back */
  .card-back__pattern {
    position: absolute; inset: 0;
    background: linear-gradient(135deg, var(--card-pattern), var(--card) 70%);
  }
  .card-back__name {
    position: absolute; right: 36px; top: 40px;
    font-weight: 700; font-size: 30px; letter-spacing: 1px; text-transform: uppercase;
  }
  /* front */
  .brand {
    position: absolute; left: 34px; top: 34px;
    display: flex; align-items: center; gap: 14px;
  }
  .brand__square { width: 18px; height: 18px; background: var(--accent); }
  .brand__name {
    font-weight: 700; font-size: 24px; line-height: 1.1;
    text-transform: uppercase; letter-spacing: .5px;
  }
  .person { position: absolute; left: 34px; top: 138px; }
  .person__name { font-weight: 600; font-size: 22px; line-height: 1.2; }
  .person__role { font-size: 12px; color: var(--ink-soft); }
  .divider {
    position: absolute; left: 34px; right: 34px; top: 200px;
    height: 1.5px; background: var(--accent);
  }
  .contact {
    position: absolute; left: 34px; top: 216px; list-style: none;
    font-size: 13px; line-height: 1.75;
  }
  .contact__item { display: flex; align-items: center; gap: 10px; }
  .contact__icon { width: 13px; height: 13px; fill: var(--accent); flex: none; }
  .address {
    position: absolute; right: 34px; top: 216px; text-align: right;
    font-size: 12px; line-height: 1.75; color: var(--ink-soft); font-style: normal;
  }
</style>
</head>
<body>
<main class="stage">
  <section class="card card-back" aria-label="Business card back">
    <div class="card-back__pattern" role="img" aria-label="Faint tone-on-tone repeating brand pattern"></div>
    <p class="card-back__name">Kestrel</p>
  </section>

  <section class="card card-front" aria-label="Business card front">
    <div class="brand">
      <span class="brand__square"></span>
      <p class="brand__name">Kestrel Roofing<br>&amp; Restoration</p>
    </div>
    <div class="person">
      <p class="person__name">Marcus L Reed</p>
      <p class="person__role">CEO</p>
    </div>
    <div class="divider"></div>
    <ul class="contact">
      <li class="contact__item">
        <svg class="contact__icon" viewBox="0 0 24 24" aria-hidden="true"><path d="M6.6 10.8a15.1 15.1 0 0 0 6.6 6.6l2.2-2.2c.3-.3.7-.4 1-.2 1.1.4 2.3.6 3.6.6.6 0 1 .4 1 1V20c0 .6-.4 1-1 1A17 17 0 0 1 3 4c0-.6.4-1 1-1h3.5c.6 0 1 .4 1 1 0 1.3.2 2.5.6 3.6.1.3 0 .7-.2 1z"/></svg>
        <span>(555) 014-22903</span>
      </li>
      <li class="contact__item">
        <svg class="contact__icon" viewBox="0 0 24 24" aria-hidden="true"><path d="M2 5h20v14H2z" fill="none"/><path d="M2 5h20v14H2V5zm2 2v.4l8 5 8-5V7H4z"/></svg>
        <span>hello@kestrelroof.com</span>
      </li>
    </ul>
    <address class="address">PO BOX 456 harbour road<br>3rd street Geelong</address>
  </section>
</main>
</body>
</html>
```